SkyWatchly - Design a new page for our website

The designer is to use our existing website to match color and style, and the documents provided to create a webpage that reflects the information in the brochure attached. This should also include a button to download our brochure and a form to request more information by entering name, phone, and email. This page will be added to our main site and will be coded by our webmaster team.

View website at: https://www.palisadecorp.example/

NOTE: The project has been upgraded to include coding.

Target Market(s)

High End Residential, Industrial, Commercial, Prisons, Public Events

Industry/Entity Type

Security Service

Coding

Coded - Design and coding required

Number of Pages Required

1 page

Font styles to use
Other font styles liked:
• Raleway & match fonts on site

Requirements
Must have
• 1. Match in color and style to our existing site as this page will be added to the existing website.

2. Place FPB Logo (attached to the brief) in a horizontal bar the width of the page with the following text: “SkyWatchly and all of Palisade's services are available under our FPB Contract." (Add button) Click for Info

3. Table showing service level options as shown in the provided brochure.

4. SkyWatchly should use the Raleway font with "SkyWatch" in bold and "ly" in regular. SkyWatchly should appear as one word.
Nice to have
• 1. Simple design expressing clean and easy to comprehend points

2. Please be creative, use the ability to scroll vertically on the page to space out the content and add supporting graphics or images.

```html
<!DOCTYPE html>
<html lang="en">
<head>
<meta charset="utf-8">
<title>SkyWatchly – Drone Risk Assessment Services</title>
<link href="https://fonts.googleapis.com/css2?family=Raleway:wght@300;400;500;600;700&display=swap" rel="stylesheet">
<style>
:root{
  --nav-blue:#3f74c6;
  --section-blue:#3d6eb8;
  --light-gray:#e9e9ea;
  --page-bg:#fafafa;
  --footer-bg:#e6e6e6;
  --red:#f20d0d;
  --green:#1fb31f;
  --advance-blue:#2f6cc0;
  --check:#27b52a;
  --text-dark:#1c1c1c;
  --text-mid:#555;
  --text-soft:#777;
  --white:#fff;
}
*{box-sizing:border-box;margin:0;padding:0}
html,body{width:1200px;height:2637px;overflow:hidden}
body{font-family:'Raleway',sans-serif;background:var(--page-bg);position:relative;color:var(--text-dark)}

/* nav */
.site-nav{position:absolute;left:0;top:0;width:1200px;height:50px;background:var(--nav-blue)}
.brand{position:absolute;left:174px;top:11px;display:flex;align-items:center;gap:10px;color:var(--white)}
.brand-mark{width:26px;height:26px;border:2px solid var(--white);border-radius:50%}
.brand-name{font-weight:400;font-size:20px;line-height:28px}
.nav-links{position:absolute;top:17px;left:596px;display:flex;gap:36px;font-size:13px;color:var(--white)}
.nav-contact{position:absolute;left:937px;top:15px;background:var(--red);color:var(--white);font-size:13px;padding:2px 6px}

/* hero */
.hero{position:absolute;left:0;top:50px;width:1200px;height:423px;
  background:linear-gradient(180deg,#3b7ddf 0%,#2e86ea 52%,#3c7fd8 53%,#4c8ddc 100%)}
.hero-bell{position:absolute;left:459px;top:15px;width:62px;height:62px;border-radius:50%;background:#1c6be0;box-shadow:0 0 12px rgba(0,40,140,.6);display:flex;align-items:center;justify-content:center}
.hero-image{position:absolute;left:185px;top:80px;width:330px;height:230px;border-radius:50%;
  background:radial-gradient(ellipse at center,#5aa4f0 0%,#3f8ce8 50%,rgba(59,125,223,0) 75%)}
.hero-title{position:absolute;left:537px;top:96px;font-size:46px;color:var(--white);line-height:1}
.hero-title b{font-weight:700}.hero-title span{font-weight:300}
.hero-sub{position:absolute;left:537px;top:138px;font-size:29px;color:var(--white);font-weight:400}
.hero-text{position:absolute;left:539px;top:176px;width:495px;font-size:12px;line-height:19.5px;color:var(--white);font-weight:300}
.btn-white{position:absolute;background:var(--white);color:#555;font-size:10px;display:flex;align-items:center;justify-content:center;border-radius:2px}

/* contract bar */
.contract-bar{position:absolute;left:0;top:473px;width:1200px;height:54px;background:#f7f7f7}
.contract-bar p{position:absolute;left:402px;top:20px;font-size:10.5px;color:#111}
.contract-btn{position:absolute;left:820px;top:17px;background:var(--red);color:var(--white);font-size:12px;padding:2px 9px}

/* feature sections */
.feature{position:absolute;left:0;width:1200px;overflow:hidden}
.feature h2{position:absolute;font-weight:400;font-size:27px;line-height:33px;text-transform:uppercase}
.feature p{position:absolute;font-size:12px;line-height:19.5px;font-weight:300}
.tech{top:527px;height:402px;background:var(--section-blue);color:var(--white)}
.tech-image{position:absolute;left:560px;top:0;width:640px;height:402px;
  background:linear-gradient(90deg,var(--section-blue) 0%,#5b8cc9 30%,#8db2dc 60%,#4f79b3 100%)}
.experts{top:929px;height:424px;background:var(--light-gray);color:#3a3a3a}
.experts-image{position:absolute;left:0;top:0;width:610px;height:424px;
  background:linear-gradient(90deg,#3d3a2f 0%,#6c6450 35%,#a9a595 65%,var(--light-gray) 100%)}
.mitigation{top:1353px;height:423px;background:var(--section-blue);color:var(--white)}
.mitigation-image{position:absolute;left:560px;top:0;width:640px;height:423px;
  background:linear-gradient(90deg,var(--section-blue) 0%,#5f87c2 45%,#7e9fcf 70%,#6f93c8 100%)}

/* levels */
.levels-head{position:absolute;left:0;top:1808px;width:1200px;text-align:center}
.levels-head h2{font-size:29px;font-weight:700;line-height:34px}
.levels-head p{font-size:25px;font-weight:400;line-height:34px}
.plan{position:absolute;top:1897px;width:288px;height:228px;border:2px solid #9a9a9a;background:var(--page-bg)}
.plan svg{position:absolute;left:124px;top:-2px}
.plan h3{position:absolute;top:50px;width:100%;text-align:center;font-size:22px;font-weight:700}
.plan .lead{position:absolute;left:25px;top:94px;width:250px;font-size:18px;line-height:22px;color:var(--text-mid)}
.plan .eg{position:absolute;left:25px;top:143px;font-size:11px;line-height:14.5px;color:var(--text-mid)}
.plan .cta{position:absolute;top:190px;left:50%;transform:translateX(-50%);background:var(--red);color:var(--white);font-size:12px;padding:1px 6px;white-space:nowrap}
.plan-basic h3{color:var(--green)}.plan-advance h3{color:var(--advance-blue)}.plan-premium h3{color:var(--red)}
.features{position:absolute;top:2156px;list-style:none;font-size:12px;color:var(--text-soft)}
.features li{height:36px;display:flex;align-items:flex-start;gap:8px}
.features .tick{width:15px;height:15px;background:var(--check);border-radius:2px;display:flex;align-items:center;justify-content:center;flex:none}
.features .info{width:12px;height:12px;border:1px solid #aaa;border-radius:50%;font-size:8px;line-height:10px;text-align:center;color:#999;margin-left:6px}
.features .plain{padding-left:22px}

/* consultation + request form */
.consult{position:absolute;left:0;top:2372px;width:1200px;text-align:center;font-size:25px}
.request-form{position:absolute;left:0;top:2418px;width:1200px;display:flex;justify-content:center;gap:12px}
.request-form input{width:150px;height:35px;border:1px solid #888;background:var(--white);font-family:'Raleway',sans-serif;font-size:11px;color:#555;padding:0 10px}
.request-form input::placeholder{color:#888}
.btn-outline{height:35px;border:1px solid #888;font-family:'Raleway',sans-serif;font-size:11px;color:#555;display:flex;align-items:center;justify-content:center;background:var(--white)}

/* footer */
.site-footer{position:absolute;left:0;top:2480px;width:1200px;height:157px;background:var(--footer-bg);border-bottom:5px solid var(--nav-blue)}
.social{position:absolute;top:71px;width:24px;height:24px;border-radius:50%}
.site-footer p{position:absolute;left:0;top:104px;width:1200px;text-align:center;font-size:12px;color:#666}
</style>
</head>
<body>

<header class="site-nav">
  <div class="brand"><span class="brand-mark"></span><span class="brand-name">Palisade Consulting</span></div>
  <nav class="nav-links"><span>About Us</span><span>Services</span><span>Core Markets</span><span>Blog</span></nav>
  <span class="nav-contact">Contact Us</span>
</header>

<section class="hero">
  <div class="hero-bell">
    <svg width="34" height="34" viewBox="0 0 24 24" fill="none" stroke="#fff" stroke-width="2" stroke-linecap="round" stroke-linejoin="round"><path d="M18 16V11a6 6 0 0 0-12 0v5l-2 2h16z"/><path d="M10 21a2 2 0 0 0 4 0"/></svg>
  </div>
  <div class="hero-image" role="img" aria-label="Quadcopter drone hovering in blue light"></div>
  <h1 class="hero-title"><b>SkyWatch</b><span>ly</span></h1>
  <div class="hero-sub">DRONE RISK ASSESSMENT SERVICES</div>
  <p class="hero-text">The threat of drones is widespread and growing, but before you start scouring the skies, look first to Palisade Consulting. This Services demystifies the emerging threat that drones present to your organization by providing a comprehensive assessment.</p>
  <span class="btn-white" style="left:541px;top:248px;width:111px;height:33px">Asses Risk Now</span>
</section>

<div class="contract-bar">
  <p>SkyWatchly and all of Palisade's services are available under our FPB Contract</p>
  <span class="contract-btn">Click for Info</span>
</div>

<section class="feature tech">
  <div class="tech-image" role="img" aria-label="Hand holding a holographic wireframe drone with interface panels"></div>
  <h2 style="left:128px;top:116px">Palisade's SkyWatchly<br>Technology</h2>
  <p style="left:129px;top:185px;width:355px">Identifies the presence of any drones flying within the vicinity of your site, classifies their type, and tracks their flight duration and trajectories.</p>
  <span class="btn-white" style="left:128px;top:267px;width:185px;height:32px;font-size:9px">Identify Drones Near You</span>
</section>

<section class="feature experts">
  <div class="experts-image" role="img" aria-label="Security team watching a wall of monitoring screens"></div>
  <h2 style="left:684px;top:118px">Based upon our findings,<br>our team of experts</h2>
  <p style="left:686px;top:187px;width:340px;color:#666">Identifies your vulnerabilities, assesses risks, and makes recommendations for risk mitigation and incident response</p>
  <span class="btn-white" style="left:684px;top:249px;width:185px;height:32px;font-size:9px">Identify Risks Now</span>
</section>

<section class="feature mitigation">
  <div class="mitigation-image" role="img" aria-label="Finger pressing an incident management plan key on a keyboard"></div>
  <h2 style="left:128px;top:121px">We can help to design and<br>implement those mitigation<br>efforts</h2>
  <p style="left:129px;top:224px;width:400px">SkyWatchly is backed by the expertise of Palisade Consulting, a team of seasoned security professionals with backgrounds in security management, law enforcement, emergency services and security technology.</p>
  <span class="btn-white" style="left:128px;top:327px;width:185px;height:32px;font-size:9px">Create Safe Envirnoment Now</span>
</section>

<div class="levels-head"><h2>THREE LEVELS</h2><p>Chose the Service that’s Right for You</p></div>

<div class="plan plan-basic" style="left:126px">
  <svg width="40" height="36" viewBox="0 0 40 36"><polyline points="0,0 20,34 40,0" fill="none" stroke="#9a9a9a" stroke-width="2"/></svg>
  <h3>Basic</h3>
  <div class="lead">For small installations and private use.</div>
  <div class="eg" style="width:150px">eg: small scale industries local school, malls, home etc.</div>
  <span class="cta">Contact Us</span>
</div>
<div class="plan plan-advance" style="left:456px">
  <svg width="40" height="36" viewBox="0 0 40 36"><polyline points="0,0 20,34 40,0" fill="none" stroke="#9a9a9a" stroke-width="2"/></svg>
  <h3>Advance</h3>
  <div class="lead">For medium scale industries and events</div>
  <div class="eg" style="width:185px">eg: Communication towers, Large manufacturing Units, electrical grids etc</div>
  <span class="cta">Contact Us</span>
</div>
<div class="plan plan-premium" style="left:785px">
  <svg width="40" height="36" viewBox="0 0 40 36"><polyline points="0,0 20,34 40,0" fill="none" stroke="#9a9a9a" stroke-width="2"/></svg>
  <h3>Premium</h3>
  <div class="lead">For Bluechip Companies, Government Installations</div>
  <div class="eg" style="width:192px">eg: Power plants, Factoreis, Dams Research Centres etc</div>
  <span class="cta">Contact Us</span>
</div>

<ul class="features" style="left:150px">
  <li><span class="tick"><svg width="11" height="11" viewBox="0 0 12 12"><polyline points="2,6 5,9 10,3" fill="none" stroke="#fff" stroke-width="2"/></svg></span>Site Vulnerability Assessment</li>
  <li><span class="tick"><svg width="11" height="11" viewBox="0 0 12 12"><polyline points="2,6 5,9 10,3" fill="none" stroke="#fff" stroke-width="2"/></svg></span>30-Day Site Drone Activity Monitoring</li>
  <li><span class="tick"><svg width="11" height="11" viewBox="0 0 12 12"><polyline points="2,6 5,9 10,3" fill="none" stroke="#fff" stroke-width="2"/></svg></span>Real-time detection<span class="info">i</span></li>
  <li><span class="tick"><svg width="11" height="11" viewBox="0 0 12 12"><polyline points="2,6 5,9 10,3" fill="none" stroke="#fff" stroke-width="2"/></svg></span>Email &amp; Text Alerts<span class="info">i</span></li>
  <li><span class="tick"><svg width="11" height="11" viewBox="0 0 12 12"><polyline points="2,6 5,9 10,3" fill="none" stroke="#fff" stroke-width="2"/></svg></span>Drone Classification<span class="info">i</span></li>
  <li><span class="tick"><svg width="11" height="11" viewBox="0 0 12 12"><polyline points="2,6 5,9 10,3" fill="none" stroke="#fff" stroke-width="2"/></svg></span>Drone Flight Statistics</li>
</ul>
<ul class="features" style="left:480px">
  <li class="plain">Everything in basic and .....</li>
  <li><span class="tick"><svg width="11" height="11" viewBox="0 0 12 12"><polyline points="2,6 5,9 10,3" fill="none" stroke="#fff" stroke-width="2"/></svg></span>Pilot Presence Detection</li>
  <li><span class="tick"><svg width="11" height="11" viewBox="0 0 12 12"><polyline points="2,6 5,9 10,3" fill="none" stroke="#fff" stroke-width="2"/></svg></span>Pilot Location</li>
  <li><span class="tick"><svg width="11" height="11" viewBox="0 0 12 12"><polyline points="2,6 5,9 10,3" fill="none" stroke="#fff" stroke-width="2"/></svg></span>Drone Location and Trajectory<span class="info">i</span></li>
  <li><span class="tick"><svg width="11" height="11" viewBox="0 0 12 12"><polyline points="2,6 5,9 10,3" fill="none" stroke="#fff" stroke-width="2"/></svg></span>Response Team Plan<span class="info">i</span></li>
</ul>
<ul class="features" style="left:810px">
  <li class="plain">Everything in basic, advance and .....</li>
  <li><span class="tick"><svg width="11" height="11" viewBox="0 0 12 12"><polyline points="2,6 5,9 10,3" fill="none" stroke="#fff" stroke-width="2"/></svg></span>Response Team Training<span class="info">i</span></li>
  <li><span class="tick"><svg width="11" height="11" viewBox="0 0 12 12"><polyline points="2,6 5,9 10,3" fill="none" stroke="#fff" stroke-width="2"/></svg></span>Mobile Command<span class="info">i</span></li>
  <li><span class="tick"><svg width="11" height="11" viewBox="0 0 12 12"><polyline points="2,6 5,9 10,3" fill="none" stroke="#fff" stroke-width="2"/></svg></span>Real-Time Event Monitoring and<span class="info">i</span></li>
  <li><span class="tick"><svg width="11" height="11" viewBox="0 0 12 12"><polyline points="2,6 5,9 10,3" fill="none" stroke="#fff" stroke-width="2"/></svg></span>Real Time Notification<span class="info">i</span></li>
</ul>

<div class="consult">Schedule A Free Consultation</div>
<form class="request-form">
  <input type="text" name="name" placeholder="Name" aria-label="Name">
  <input type="tel" name="phone" placeholder="Phone" aria-label="Phone">
  <input type="email" name="email" placeholder="Email" aria-label="Email">
  <button type="submit" class="btn-outline" style="width:111px">Book Now</button>
  <span class="btn-outline" style="width:147px">Download Our Broucher</span>
</form>

<footer class="site-footer">
  <span class="social" style="left:566px;background:#3b5fa8"></span>
  <span class="social" style="left:609px;background:#2a86c8"></span>
  <p>Privacy Policy |© 2020 Palisade Consulting. All Rights Reserved.</p>
</footer>

</body>
</html>
```